依頼詳細
スタンダードメニューと特別ページメニューの作成。
スタンダードメニューはフランチャイズ店のようなイメージでお願いします。
参考サイト
https://www.mitsukeru-kensaku.example/search?q=%E5%B1%85%E9%85%92%E5%B1%8B%E3%83%A1%E3%83%8B%E3%83%A5%E3%83%BC&tbm=isch#imgrc=Qx7mTa2Lp9%3Bhttp%253A%252F%252Fimg.tarunikki.example%252Fphoto%252F5.jpg%3Bhttp%253A%252F%252Fkazuenikki.tarunikki.example%252F2011%252F10%252Fpost_17.html
この写真の上の部分の感じです。
料理写真と値段はエクセルで添付致します。
そのほかの写真はホームページから使用してください。
http://www.kurotori-shokudo.example/
料理の説明のあるものもありますので参考にして下さい。
エクセルシート1、2に分けて記載してあります。
よろしくお願い致します。

サイズ
A4
ページ数
6ページ
希望イメージ
シンプル 複雑
単色 カラフル
暗い 明るい
日常 高級
遊び心 厳粛
未来的 伝統的
女性的 男性的
希望する色
赤 黄 黒
納品ファイル
• イラストレーター形式 (.ai)
補足説明
かなり急いでいます。早ければ早いほど助かります。
写真を入れた簡単なイメージだけでも本日12時半頃までに頂けるとそのあとは2、3日の余裕はできます。
宜しくお願いします。

```html
<!DOCTYPE html>
<html lang="ja">
<head>
<meta charset="utf-8">
<title>メニュー</title>
<link rel="stylesheet" href="https://fonts.googleapis.com/css2?family=Noto+Sans+JP:wght@500;700;900&display=swap">
<style>
:root{
  --ink:#0d0b0a;
  --red:#c4161c;
  --red-dark:#7a0c0f;
  --white:#ffffff;
  --label:#f2f2f2;
  --label-ink:#1a1a1a;
}
*{margin:0;padding:0;box-sizing:border-box}
html,body{width:849px;height:1200px;overflow:hidden;background:var(--ink)}
body{font-family:"Noto Sans JP",sans-serif}
.menu-page{position:relative;width:849px;height:1200px;background:var(--ink)}
.band{background:linear-gradient(var(--red),var(--red-dark));height:14px}
.band--foot{height:48px}
.section{position:relative;height:370px;display:flex;padding:6px 12px 6px 12px;gap:6px}
.hero{position:relative;width:246px;height:358px;border-radius:2px}
.hero--salad{background:radial-gradient(circle at 55% 60%,#8fb66a,#4d6e33 55%,#2a2a22)}
.hero--sashimi{background:radial-gradient(circle at 50% 65%,#f0c9b8,#c98a7c 50%,#3b302c)}
.hero--grill{background:radial-gradient(circle at 50% 65%,#9a7440,#5a3e1f 55%,#1e1710)}
.badge{position:absolute;left:12px;top:12px;width:104px;height:104px;border-radius:50%;
  background:var(--red);color:var(--white);display:flex;flex-direction:column;
  align-items:center;justify-content:center;font-weight:900;border:3px solid var(--white)}
.badge__main{font-size:30px;line-height:1}
.badge--large .badge__main{font-size:40px}
.badge--light{background:var(--white);color:var(--red);border-color:var(--red)}
.badge--light .badge__main{font-size:44px}
.badge__sub{font-size:16px;margin-top:2px}
.grid{flex:1;display:grid;grid-template-columns:repeat(5,1fr);grid-template-rows:1fr 1fr;gap:4px}
.dish{position:relative;display:flex;flex-direction:column}
.dish__photo{flex:1;border-radius:2px}
.p1{background:linear-gradient(160deg,#c0452c,#6e1e12)}
.p2{background:linear-gradient(160deg,#e7dfa4,#a89a4a)}
.p3{background:linear-gradient(160deg,#e38a4a,#a9411d)}
.p4{background:linear-gradient(160deg,#d8413a,#7aa144)}
.p5{background:linear-gradient(160deg,#b85a2f,#5a2a12)}
.p6{background:linear-gradient(160deg,#7d9a54,#3c4f25)}
.p7{background:linear-gradient(160deg,#e9e2cf,#a79c7c)}
.p8{background:linear-gradient(160deg,#7fbf8a,#3e6e49)}
.p9{background:linear-gradient(160deg,#c8d88a,#6d8a3a)}
.p10{background:linear-gradient(160deg,#b97a45,#5c3a1e)}
.dish__name{position:absolute;left:4px;right:4px;bottom:34px;background:var(--label);color:var(--label-ink);
  font-size:11px;font-weight:700;text-align:center;line-height:16px;white-space:nowrap}
.dish__name--two-line{line-height:14px;padding:1px 0}
.dish__price{height:32px;text-align:right;padding-right:6px;color:var(--red);font-weight:900;font-size:24px;line-height:32px;
  text-shadow:0 0 2px var(--white),0 0 2px var(--white),0 0 2px var(--white)}
.dish__price small{font-size:16px}
</style>
</head>
<body>
<main class="menu-page">
  <div class="band"></div>

  <section class="section">
    <div class="hero hero--salad" role="img" aria-label="サラダの料理写真">
      <div class="badge"><span class="badge__main">サラダ</span></div>
    </div>
    <div class="grid">
      <div class="dish"><div class="dish__photo p1" role="img" aria-label="まるきゅうの写真"></div><p class="dish__name">まるきゅう(一本)</p><p class="dish__price">199<small>円</small></p></div>
      <div class="dish"><div class="dish__photo p2" role="img" aria-label="トマトスライスの写真"></div><p class="dish__name">トマトスライス</p><p class="dish__price">329<small>円</small></p></div>
      <div class="dish"><div class="dish__photo p3" role="img" aria-label="ホッキ貝サラダの写真"></div><p class="dish__name">ホッキ貝サラダ</p><p class="dish__price">399<small>円</small></p></div>
      <div class="dish"><div class="dish__photo p4" role="img" aria-label="たっぷりキャベツの写真"></div><p class="dish__name">たっぷりキャベツ</p><p class="dish__price">399<small>円</small></p></div>
      <div class="dish"><div class="dish__photo p5" role="img" aria-label="大根サラダの写真"></div><p class="dish__name">大根サラダ</p><p class="dish__price">550<small>円</small></p></div>
      <div class="dish"><div class="dish__photo p6" role="img" aria-label="ねぎジャコサラダの写真"></div><p class="dish__name">ねぎジャコサラダ</p><p class="dish__price">550<small>円</small></p></div>
      <div class="dish"><div class="dish__photo p7" role="img" aria-label="豆腐サラダの写真"></div><p class="dish__name">豆腐サラダ</p><p class="dish__price">550<small>円</small></p></div>
      <div class="dish"><div class="dish__photo p8" role="img" aria-label="ねばねばサラダの写真"></div><p class="dish__name">ねばねばサラダ</p><p class="dish__price">399<small>円</small></p></div>
      <div class="dish"><div class="dish__photo p9" role="img" aria-label="レタスねぎジャコサラダの写真"></div><p class="dish__name dish__name--two-line">レタス<br>ねぎジャコサラダ</p><p class="dish__price">399<small>円</small></p></div>
      <div class="dish"><div class="dish__photo p10" role="img" aria-label="鳥鳥サラダの写真"></div><p class="dish__name">鳥鳥サラダ</p><p class="dish__price">720<small>円</small></p></div>
    </div>
  </section>

  <div class="band"></div>

  <section class="section">
    <div class="hero hero--sashimi" role="img" aria-label="刺身の料理写真">
      <div class="badge badge--large"><span class="badge__main">刺身</span></div>
    </div>
    <div class="grid">
      <div class="dish"><div class="dish__photo p1" role="img" aria-label="まるきゅうの写真"></div><p class="dish__name">まるきゅう(一本)</p><p class="dish__price">199<small>円</small></p></div>
      <div class="dish"><div class="dish__photo p2" role="img" aria-label="トマトスライスの写真"></div><p class="dish__name">トマトスライス</p><p class="dish__price">329<small>円</small></p></div>
      <div class="dish"><div class="dish__photo p3" role="img" aria-label="ホッキ貝サラダの写真"></div><p class="dish__name">ホッキ貝サラダ</p><p class="dish__price">399<small>円</small></p></div>
      <div class="dish"><div class="dish__photo p4" role="img" aria-label="たっぷりキャベツの写真"></div><p class="dish__name">たっぷりキャベツ</p><p class="dish__price">399<small>円</small></p></div>
      <div class="dish"><div class="dish__photo p5" role="img" aria-label="大根サラダの写真"></div><p class="dish__name">大根サラダ</p><p class="dish__price">550<small>円</small></p></div>
      <div class="dish"><div class="dish__photo p6" role="img" aria-label="ねぎジャコサラダの写真"></div><p class="dish__name">ねぎジャコサラダ</p><p class="dish__price">550<small>円</small></p></div>
      <div class="dish"><div class="dish__photo p7" role="img" aria-label="豆腐サラダの写真"></div><p class="dish__name">豆腐サラダ</p><p class="dish__price">550<small>円</small></p></div>
      <div class="dish"><div class="dish__photo p8" role="img" aria-label="ねばねばサラダの写真"></div><p class="dish__name">ねばねばサラダ</p><p class="dish__price">399<small>円</small></p></div>
      <div class="dish"><div class="dish__photo p9" role="img" aria-label="レタスねぎジャコサラダの写真"></div><p class="dish__name dish__name--two-line">レタス<br>ねぎジャコサラダ</p><p class="dish__price">399<small>円</small></p></div>
      <div class="dish"><div class="dish__photo p10" role="img" aria-label="鳥鳥サラダの写真"></div><p class="dish__name">鳥鳥サラダ</p><p class="dish__price">720<small>円</small></p></div>
    </div>
  </section>

  <div class="band"></div>

  <section class="section">
    <div class="hero hero--grill" role="img" aria-label="炭火焼の料理写真">
      <div class="badge badge--light"><span class="badge__main">焼</span><span class="badge__sub">炭火焼</span></div>
    </div>
    <div class="grid">
      <div class="dish"><div class="dish__photo p1" role="img" aria-label="まるきゅうの写真"></div><p class="dish__name">まるきゅう(一本)</p><p class="dish__price">199<small>円</small></p></div>
      <div class="dish"><div class="dish__photo p2" role="img" aria-label="トマトスライスの写真"></div><p class="dish__name">トマトスライス</p><p class="dish__price">329<small>円</small></p></div>
      <div class="dish"><div class="dish__photo p3" role="img" aria-label="ホッキ貝サラダの写真"></div><p class="dish__name">ホッキ貝サラダ</p><p class="dish__price">399<small>円</small></p></div>
      <div class="dish"><div class="dish__photo p4" role="img" aria-label="たっぷりキャベツの写真"></div><p class="dish__name">たっぷりキャベツ</p><p class="dish__price">399<small>円</small></p></div>
      <div class="dish"><div class="dish__photo p5" role="img" aria-label="大根サラダの写真"></div><p class="dish__name">大根サラダ</p><p class="dish__price">550<small>円</small></p></div>
      <div class="dish"><div class="dish__photo p6" role="img" aria-label="ねぎジャコサラダの写真"></div><p class="dish__name">ねぎジャコサラダ</p><p class="dish__price">550<small>円</small></p></div>
      <div class="dish"><div class="dish__photo p7" role="img" aria-label="豆腐サラダの写真"></div><p class="dish__name">豆腐サラダ</p><p class="dish__price">550<small>円</small></p></div>
      <div class="dish"><div class="dish__photo p8" role="img" aria-label="ねばねばサラダの写真"></div><p class="dish__name">ねばねばサラダ</p><p class="dish__price">399<small>円</small></p></div>
      <div class="dish"><div class="dish__photo p9" role="img" aria-label="レタスねぎジャコサラダの写真"></div><p class="dish__name dish__name--two-line">レタス<br>ねぎジャコサラダ</p><p class="dish__price">399<small>円</small></p></div>
      <div class="dish"><div class="dish__photo p10" role="img" aria-label="鳥鳥サラダの写真"></div><p class="dish__name">鳥鳥サラダ</p><p class="dish__price">720<small>円</small></p></div>
    </div>
  </section>

  <div class="band band--foot"></div>
</main>
</body>
</html>
```